Amber Reed Wellness Buisness Cards

I am looking to create a business card for a healing business. In the business I provide coaching and Reiki. I am a licensed LCPC (licensed clinical professional counselor)

Amber Reed Wellness
Soul Centered Healing, Reiki Healinig

Lena Dovrahi, L.C.P.C

The card should include the following
biz name: Amber Reed Wellness
my name: Lena Dovrahi
website: Lenadovrahi.example
email: lena.pastum@mailbox.example
instagram handle: lenapastumdovrahi

Target Market(s)

Women ages 25-65

```html
<!DOCTYPE html>
<html lang="en">
<head>
<meta charset="utf-8">
<title>Amber Reed Wellness – Business Cards</title>
<link rel="stylesheet" href="https://fonts.googleapis.com/css2?family=Open+Sans:wght@400;600;700&family=Roboto+Condensed:wght@400&display=swap">
<style>
  :root {
    --backdrop: #2a2a2a;
    --card-white: #ffffff;
    --leaf-green: #6b9b2a;
    --amber: #d6b833;
    --ink: #3d3d3d;
    --rule: #d4d4d4;
    --gradient-top: #dcc23b;
    --gradient-bottom: #6a9a27;
    --on-color: #ffffff;
  }
  * { box-sizing: border-box; margin: 0; padding: 0; }
  html, body {
    width: 1200px; height: 1200px; overflow: hidden;
    background: var(--backdrop);
  }
  .canvas { position: relative; width: 1200px; height: 1200px; }
  .card {
    position: absolute; top: 310px; width: 364px; height: 594px;
    box-shadow: 0 3px 8px rgba(0,0,0,.45);
  }
  .card--front { left: 234px; background: var(--card-white); }
  .card--back {
    left: 627px; width: 369px;
    background: linear-gradient(to bottom, var(--gradient-top), var(--gradient-bottom));
  }

  /* Front */
  .brand {
    position: absolute; top: 92px; left: 0; right: 0;
    display: flex; flex-direction: column; align-items: center; gap: 22px;
  }
  .brand__dot { width: 96px; height: 96px; border-radius: 50%; background: var(--leaf-green); }
  .brand__name {
    font-family: "Open Sans", sans-serif; font-weight: 700; font-size: 30px;
    line-height: 1.15; letter-spacing: .5px; text-align: center;
    color: var(--leaf-green); text-transform: uppercase;
  }
  .holder {
    position: absolute; top: 418px; left: 0; right: 0; text-align: center;
    font-family: "Open Sans", sans-serif; font-weight: 700; font-size: 25px;
    color: var(--leaf-green); letter-spacing: .3px;
  }
  .holder__surname { color: var(--amber); }
  .holder__rule {
    position: absolute; top: 462px; left: 73px; width: 218px; height: 1px; background: var(--rule);
  }
  .contact {
    position: absolute; top: 477px; left: 0; right: 0; text-align: center;
    font-family: "Open Sans", sans-serif; font-size: 16px; line-height: 21px; color: var(--ink);
  }
  .contact__label { color: var(--leaf-green); }
  .contact__accent { color: var(--amber); }

  /* Back */
  .back-brand {
    position: absolute; top: 190px; left: 0; right: 0;
    display: flex; flex-direction: column; align-items: center; gap: 22px;
  }
  .back-brand__dot { width: 110px; height: 110px; border-radius: 50%; background: var(--on-color); }
  .back-brand__name {
    font-family: "Open Sans", sans-serif; font-weight: 700; font-size: 30px;
    line-height: 1.15; text-align: center; color: var(--on-color); text-transform: uppercase;
  }
  .services {
    position: absolute; top: 476px; left: 0; right: 0; text-align: center; list-style: none;
    font-family: "Roboto Condensed", sans-serif; font-size: 17px; line-height: 24.5px;
    color: var(--on-color); text-transform: uppercase;
  }
</style>
</head>
<body>
<main class="canvas">
  <section class="card card--front" aria-label="Business card front">
    <div class="brand">
      <span class="brand__dot"></span>
      <p class="brand__name">Amber Reed<br>Wellness</p>
    </div>
    <h1 class="holder">LENA <span class="holder__surname">DOVRAHI</span></h1>
    <div class="holder__rule"></div>
    <p class="contact">
      <span class="contact__label">www.</span><span class="contact__accent">Lenadovrahi</span><span class="contact__label">.example</span><br>
      <span class="contact__label">E:</span> lena.pastum@mailbox.example<br>
      <span class="contact__label">INSTAGRAM:</span> lenapastumdovrahi
    </p>
  </section>

  <section class="card card--back" aria-label="Business card back">
    <div class="back-brand">
      <span class="back-brand__dot"></span>
      <p class="back-brand__name">Amber Reed<br>Wellness</p>
    </div>
    <ul class="services">
      <li>Soul Centered Coaching</li>
      <li>Reiki Healing</li>
      <li>Certified Crystal Reiki Master</li>
    </ul>
  </section>
</main>
</body>
</html>
```